TALLOWBROOK FREIGHT & PLANT HIRE NEEDS A FLYER

WE NEED A FLYER FOR OUR COMPANY <br/>WE SPECIALISE IN ROAD BUILDING AND MAINTENANCE, GENERAL EARTHWORK DAM REPAIRS & DESILTING, FENCE CLEARING, FIRE BREAKS, GRAVEL SOURCE AND DELIVERY GENERAL FREIGHT STEEL HAY LICK AND MCHINERY. <br/><br/>I HAVE UPLOAD A FILE THAT I LIKE AND WOULD LIKE SOMETHING THE SAME IF POSSIBLE. AND LOGO TO GO WITH IT.

```html
<!DOCTYPE html>
<html lang="en">
<head>
<meta charset="utf-8">
<title>Tallowbrook Freight &amp; Plant Hire – Flyer</title>
<link rel="stylesheet" href="https://fonts.googleapis.com/css2?family=Oswald:wght@300;400;500;600&display=swap">
<style>
  :root {
    --charcoal: #3a3a3c;
    --charcoal-deep: #2f2f31;
    --yellow: #fbb615;
    --orange: #f3a51f;
    --paper: #ffffff;
    --paper-shade: #ececec;
    --list-text: #ffffff;
    --tick-box: #bfbfbf;
    --hatch: #e4e4e4;
  }
  * { box-sizing: border-box; margin: 0; padding: 0; }
  html, body { width: 921px; height: 1200px; overflow: hidden; background: var(--paper); }
  .flyer {
    position: relative;
    width: 921px;
    height: 1200px;
    overflow: hidden;
    font-family: "Oswald", "Arial Narrow", sans-serif;
    background: radial-gradient(ellipse at 50% 35%, var(--paper) 55%, var(--paper-shade) 100%);
  }
  .flyer__shapes { position: absolute; inset: 0; }
  .top-band {
    position: absolute; left: 0; top: 0; width: 100%; height: 89px;
    background: var(--charcoal);
    display: flex; align-items: center; justify-content: center;
    color: var(--yellow); font-weight: 400; font-size: 38px; letter-spacing: 0.5px;
  }
  .machine-photo {
    position: absolute; left: 590px; top: 445px; width: 300px; height: 175px;
    border-radius: 12px 12px 6px 6px;
    background: linear-gradient(160deg, #5a5a5a 0%, #3c3c3c 35%, #f2b31c 60%, #d99a0c 100%);
    opacity: 0.9;
  }
  .brand {
    position: absolute; left: 0; width: 921px; top: 175px;
    text-align: center; color: var(--charcoal); font-weight: 600; line-height: 1;
  }
  .brand__name { font-size: 118px; letter-spacing: 1px; color: var(--orange); }
  .brand__sub { font-size: 62px; margin-top: 18px; }
  .brand__suffix { font-size: 42px; margin-top: 14px; }
  .column { position: absolute; top: 642px; }
  .column--services { left: 67px; }
  .column--machinery { left: 475px; }
  .column__title { color: var(--orange); font-weight: 500; font-size: 31px; margin-bottom: 12px; }
  .checklist { list-style: none; }
  .checklist li {
    position: relative; padding-left: 37px;
    color: var(--list-text); font-weight: 300; font-size: 22px; line-height: 29.2px;
  }
  .checklist li::before {
    content: ""; position: absolute; left: 3px; top: 9px;
    width: 13px; height: 13px; border: 1.5px solid var(--tick-box); border-radius: 2px;
  }
  .checklist li::after {
    content: ""; position: absolute; left: 8px; top: 8px;
    width: 6px; height: 11px;
    border-right: 2.5px solid var(--yellow); border-bottom: 2.5px solid var(--yellow);
    transform: rotate(40deg);
  }
  .contact {
    position: absolute; left: 520px; top: 1032px; width: 390px;
    color: var(--charcoal); text-align: center;
  }
  .contact__names { font-size: 33px; font-weight: 400; }
  .contact__phone {
    display: flex; align-items: center; justify-content: center; gap: 10px;
    font-size: 46px; font-weight: 500; margin-top: 2px;
  }
  .contact__phone svg { width: 34px; height: 34px; }
  .contact__email { font-size: 25px; font-weight: 400; margin-top: 6px; white-space: nowrap; }
  .contact__email span { font-size: 19px; font-weight: 500; }
  .seal {
    position: absolute; left: 327px; top: 1012px; width: 120px; height: 120px;
    border-radius: 50%; background: radial-gradient(circle, #8a8a8a 0%, #5b5b5b 70%, #d0d0d0 72%, #9a9a9a 100%);
  }
</style>
</head>
<body>
<main class="flyer">
  <svg class="flyer__shapes" width="921" height="1200" viewBox="0 0 921 1200" aria-hidden="true">
    <polygon points="0,490 921,622 921,1200 0,1200" fill="var(--charcoal)"/>
    <polygon points="39,1200 472,1043 472,1200" fill="var(--hatch)"/>
    <polygon points="472,1043 921,907 921,1200 472,1200" fill="var(--yellow)"/>
  </svg>

  <header class="top-band">FOR ALL YOU FREIGHT AND PLANT HIRE NEEDS!</header>

  <div class="machine-photo" role="img" aria-label="Yellow forklift photograph"></div>

  <div class="brand">
    <div class="brand__name">TALLOWBROOK</div>
    <div class="brand__sub">FREIGHT &amp; PLANT HIRE</div>
    <div class="brand__suffix">PTY LTD</div>
  </div>

  <section class="column column--services">
    <h2 class="column__title">SPECIALISING IN:</h2>
    <ul class="checklist">
      <li>ROAD BUILDING AND MAINTENANCE</li>
      <li>GENERAL EARTHWORKS</li>
      <li>DAM REPAIRS &amp; DESILTING</li>
      <li>FENCE CLEARING</li>
      <li>FIRE BREAKS</li>
      <li>GRAVEL SOURCE &amp; DELIVERY</li>
      <li>GENERAL FREIGHT</li>
      <li>STEEL</li>
      <li>LICK</li>
      <li>HAY</li>
      <li>MACHINERY</li>
    </ul>
  </section>

  <section class="column column--machinery">
    <h2 class="column__title">CURRENT MACHINERY AVAILABLE:</h2>
    <ul class="checklist">
      <li>GRADER</li>
      <li>LOADER &amp; STICK RAKE</li>
      <li>ROLLERS DOZER</li>
      <li>WATER TRUCKS</li>
      <li>SIDE TIPPERS</li>
      <li>PRIME MOVERS</li>
      <li>FORKLIFT</li>
      <li>SKID STEER LOADER</li>
      <li>FLAT TOPS</li>
      <li>DROP DECK</li>
    </ul>
  </section>

  <div class="seal" aria-hidden="true"></div>

  <footer class="contact">
    <div class="contact__names">DEAN &amp; MARISSA CALLOWAY</div>
    <div class="contact__phone">
      <svg viewBox="0 0 24 24" aria-hidden="true"><path fill="var(--charcoal)" d="M6.6 10.8a15.2 15.2 0 0 0 6.6 6.6l2.2-2.2a1 1 0 0 1 1-.25 11.4 11.4 0 0 0 3.6.57 1 1 0 0 1 1 1V20a1 1 0 0 1-1 1A17 17 0 0 1 3 4a1 1 0 0 1 1-1h3.5a1 1 0 0 1 1 1c0 1.25.2 2.45.57 3.6a1 1 0 0 1-.25 1z"/><path fill="none" stroke="var(--charcoal)" stroke-width="1.8" stroke-linecap="round" d="M15 3.5a6 6 0 0 1 5.5 5.5M15 7a2.6 2.6 0 0 1 2 2"/></svg>
      0412558093
    </div>
    <div class="contact__email"><span>EMAIL:</span> marissa@tallowbrookfreight.com.au</div>
  </footer>
</main>
</body>
</html>
```